Brivon Australia Dental

I need to update my website and design. I have some ideas in mind and would like to replicate the format from another website into my own. I need the website to be easy to edit (I have no prior wordpress exp) after the design is complete. Please visit https://thelittlenestcare.org.au/ for example of layout.
Target Market(s)
Parents and elder folks
Industry/Entity Type
Dental
Coding
Coded - Design and coding required
Number of Pages Required
4 page
Font styles to use
Sans Serif
Colors
0392cd
Requirements
Must have
- - Home, Services, About Us, News
- - Colours
- - Clear action from viewers
- - Location of business (able to change all the time)
- - Illustrations/ photos

```html
<!DOCTYPE html>
<html lang="en">
<head>
<meta charset="utf-8">
<title>Brivon Australia Dental</title>
<link rel="stylesheet" href="https://fonts.googleapis.com/css2?family=Hind:wght@300;400;500;600;700&display=swap">
<style>
:root{
  --blue:#0392cd;
  --blue-dark:#0679b0;
  --blue-soft:#b9e2f2;
  --blue-pale:#e3f3fa;
  --ink:#222831;
  --text:#5b6168;
  --grey-band:#f3f4f6;
  --panel:#eef2f5;
  --pattern:#f2f4f6;
  --footer:#1f2226;
  --white:#ffffff;
}
*{box-sizing:border-box;margin:0;padding:0}
html,body{width:1200px;height:3904px;overflow:hidden}
body{position:relative;background:var(--white);font-family:"Hind",sans-serif;color:var(--text)}
.abs{position:absolute}
.btn{position:absolute;display:flex;align-items:center;justify-content:center;background:var(--blue);color:var(--white);font-size:15px;font-weight:500;letter-spacing:.5px;box-shadow:3px 4px 8px rgba(0,0,0,.22)}
.heading{font-weight:300;color:var(--blue);letter-spacing:1px}
.heading b{font-weight:600}
.eyebrow{font-size:15px;color:var(--ink)}
.photo{position:absolute}

/* header */
.logo-tab{left:533px;top:0;width:134px;height:94px;background:linear-gradient(180deg,#4ba6d8,#6c8fd0);border-radius:0 0 67px 67px;display:flex;align-items:center;justify-content:center;color:var(--white);font-size:22px;font-weight:500;z-index:3}
.nav{left:224px;top:103px;width:750px;height:52px;z-index:2}
.nav-links{position:absolute;left:0;top:0;width:750px;height:52px;font-size:13px;font-weight:500;color:var(--white)}
.nav-links span{position:absolute;top:19px}
.nav-links .active{text-decoration:underline}
.hero-photo{left:0;top:129px;width:1200px;height:424px;background:linear-gradient(90deg,#eef5fb 0%,#dde9f3 40%,#c9d9e6 65%,#e6cfc4 85%,#efe1da 100%)}
.hero-text{left:224px;top:264px;width:420px}
.hero-text .eyebrow{font-size:15px;text-decoration:underline}
.hero-title{font-size:35px;font-weight:600;color:var(--blue);letter-spacing:1px;margin-top:6px;line-height:1.2}
.hero-sub{font-size:15px;color:var(--ink);line-height:1.25;margin-top:8px}
.feature{position:absolute;top:515px;width:238px;height:79px;background:var(--white);border-radius:40px 8px 8px 40px;box-shadow:2px 4px 10px rgba(0,0,0,.15)}
.feature .dot{position:absolute;left:4px;top:4px;width:71px;height:71px;border-radius:50%;background:var(--blue);border:3px solid var(--white);box-shadow:0 0 0 1px #d9eef7;display:flex;align-items:center;justify-content:center}
.feature .dot::after{content:"";width:34px;height:34px;border-radius:50%;border:2px solid var(--white)}
.feature h4{position:absolute;left:88px;top:23px;font-size:12px;font-weight:500;color:var(--blue);letter-spacing:.5px}
.feature p{position:absolute;left:88px;top:39px;font-size:10px;line-height:1.15;color:var(--text)}

/* about */
.about-photo{left:0;top:629px;width:470px;height:313px;background:linear-gradient(120deg,#e7eef3,#cfe0ea 45%,#5ab0d6 70%,#e9eef2)}
.about-text{left:494px;top:680px;width:480px}
.about-text .heading{font-size:29px;margin-top:2px}
.about-text p{font-size:12.5px;line-height:1.3;text-align:justify;margin-top:8px;letter-spacing:.3px}

/* services */
.services-head{left:0;top:1000px;width:1200px;text-align:center}
.services-head .heading{font-size:29px;margin-top:2px}
.services-band{left:0;top:1110px;width:1200px;height:504px;background:var(--grey-band)}
.service-grid{left:224px;top:1106px;width:750px;display:grid;grid-template-columns:repeat(4,184px);gap:6px 4px}
.service{position:relative;height:254px;background:var(--white);border:1px solid #e8e9eb;text-align:center}
.service .icon{width:70px;height:70px;border-radius:50%;background:var(--blue-soft);margin:18px auto 0;box-shadow:0 3px 6px rgba(0,0,0,.12);border:3px solid var(--white);display:flex;align-items:center;justify-content:center}
.service .icon::after{content:"";width:34px;height:34px;border-radius:50%;border:2px solid var(--blue);background:var(--blue-pale)}
.service.active .icon{background:var(--blue)}
.service.active .icon::after{border-color:var(--white);background:transparent}
.service h3{font-size:15px;font-weight:600;color:var(--ink);margin-top:30px;letter-spacing:.4px}
.service.active h3{color:var(--blue)}
.service p{font-size:11.5px;line-height:1.35;margin-top:12px}
.service .bar{position:absolute;left:82px;bottom:10px;width:20px;height:2px;background:var(--blue)}

/* newsletter */
.newsletter{left:0;top:1674px;width:1200px;height:143px;background:var(--blue)}
.newsletter h2{position:absolute;top:22px;width:100%;text-align:center;font-size:28px;font-weight:400;color:var(--white);letter-spacing:1.5px}
.field-mail{position:absolute;left:386px;top:74px;width:291px;height:41px;background:var(--white);font-size:12px;color:#888;padding:13px 0 0 15px;box-shadow:2px 3px 6px rgba(0,0,0,.2)}
.submit{position:absolute;left:685px;top:74px;width:129px;height:41px;background:var(--blue-soft);color:var(--blue-dark);font-size:15px;font-weight:600;display:flex;align-items:center;justify-content:center;box-shadow:2px 3px 6px rgba(0,0,0,.2)}

/* patients */
.patient-text{left:224px;top:1980px;width:330px}
.patient-text .heading{font-size:29px;margin-top:4px}
.patient-text p{font-size:11.5px;line-height:1.35;margin-top:10px}
.pattern-area{left:606px;top:1863px;width:406px;height:523px;background:var(--pattern)}
.patient-frame{left:800px;top:1893px;width:233px;height:463px;background:var(--white);box-shadow:0 2px 8px rgba(0,0,0,.12)}
.patient-one{left:618px;top:1836px;width:173px;height:436px;background:linear-gradient(180deg,#8a6a55,#d9b79e 40%,#e8cdb8)}
.patient-card{position:absolute;left:618px;top:2125px;width:173px;height:147px;background:rgba(40,40,42,.92);padding:55px 0 0 14px}
.patient-card h5{font-size:16px;font-weight:400;color:var(--blue);letter-spacing:1px}
.patient-card p{font-size:9px;color:var(--white);line-height:1.3;margin-top:4px}
.patient-card span{display:block;font-size:10px;color:var(--blue);margin-top:6px}
.patient-two{left:800px;top:1909px;width:174px;height:433px;background:linear-gradient(180deg,#6b4a3c,#c79c84 45%,#e6c6b2)}
.patient-two-name{left:800px;top:2290px;width:174px;text-align:center;font-size:17px;color:var(--white);letter-spacing:.5px}

/* care */
.care-bg{left:0;top:2404px;width:1200px;height:332px;background:#f8f9fa}
.care-photo{left:0;top:2404px;width:554px;height:332px;background:linear-gradient(110deg,#dde6ec,#bfd4e2 40%,#8fc4e4 60%,#e5c8b6)}
.care-text{left:601px;top:2460px;width:374px}
.care-text .heading{font-size:29px}
.care-text h4{font-size:16px;font-weight:500;color:var(--ink);line-height:1.1;margin-top:12px;letter-spacing:.4px}
.care-text p{font-size:11.5px;line-height:1.4;margin-top:16px;text-align:justify}

/* appointment */
.appoint-bg{left:0;top:2736px;width:1200px;height:339px;background:var(--panel)}
.appoint-title{left:224px;top:2772px;font-size:28px}
.input{position:absolute;background:var(--white);border:1px solid #d6dadf;font-size:10px;color:#555;padding:11px 0 0 12px}
.family-photo{left:674px;top:2736px;width:526px;height:339px;background:linear-gradient(90deg,#eef2f5,#e6d4c8 30%,#f1f1f1 60%,#e8d3c6 85%,#eef2f5)}

/* news */
.news-title{left:0;top:3135px;width:1200px;text-align:center;font-size:28px}
.news-card{position:absolute;top:3200px;width:185px;height:209px;background:var(--white);box-shadow:0 2px 6px rgba(0,0,0,.12)}
.news-card .pic{height:122px}
.news-card .date{font-size:9px;color:var(--text);margin:14px 0 0 6px}
.news-card h5{font-size:12.5px;font-weight:600;color:var(--ink);line-height:1.2;margin:3px 8px 0 6px;letter-spacing:.3px}
.news-card a{display:block;font-size:10.5px;color:var(--blue);margin:8px 0 0 6px;text-decoration:none}

/* footer */
.footer{left:0;top:3538px;width:1200px;height:366px;background:var(--footer)}
.footer-logo{left:224px;top:3538px;width:132px;height:91px;background:linear-gradient(180deg,#4ba6d8,#6c8fd0);border-radius:0 0 66px 66px;display:flex;align-items:center;justify-content:center;color:var(--white);font-size:21px;font-weight:500}
.footer-about{left:226px;top:3680px;width:226px;font-size:12.5px;line-height:1.25;color:#c9cdd2;letter-spacing:1px;text-align:justify}
.social{position:absolute;top:3752px;width:26px;height:26px;border-radius:50%;background:var(--blue);border:2px solid var(--white)}
.col-title{position:absolute;top:3648px;font-size:15px;color:var(--white);letter-spacing:.8px}
.quick{left:486px;top:3684px;font-size:11px;color:var(--white);line-height:20.5px}
.contact-row{position:absolute;left:604px;font-size:11px;color:var(--white);line-height:1.2;display:flex;gap:10px;align-items:flex-start}
.hours{left:788px;top:3619px;width:186px;height:196px;border:1px solid var(--blue);padding:28px 0 0 14px}
.hours h6{font-size:15px;font-weight:400;color:var(--white);letter-spacing:.5px}
.hours table{margin-top:8px;border-collapse:collapse;font-size:10.5px;color:var(--white)}
.hours td{height:21px;padding:0 8px 0 0;white-space:nowrap}
.footer-rule{left:224px;top:3862px;width:750px;height:1px;background:#3c4147}
.copyright{left:0;top:3878px;width:1200px;text-align:center;font-size:8.5px;color:#cfd3d8}
</style>
</head>
<body>

<!-- header -->
<div class="abs logo-tab">Brivon</div>
<div class="photo hero-photo" role="img" aria-label="Smiling woman resting her chin on her hands, soft clinic background"></div>
<div class="abs nav">
  <svg width="750" height="52" viewBox="0 0 750 52"><polygon points="22,0 728,0 750,26 728,52 22,52 0,26" fill="#0392cd"/></svg>
  <div class="nav-links">
    <span class="active" style="left:223px">Home</span>
    <span style="left:312px">Services</span>
    <span style="left:415px">About Us</span>
    <span style="left:524px">News</span>
  </div>
</div>
<div class="abs hero-text">
  <div class="eyebrow">Welcome to our Dental Clinic</div>
  <div class="hero-title">Complete Dental Care</div>
  <div class="hero-sub">We offer top quality dental treatments &amp; services<br>for healthy and beautiful smiles.</div>
</div>
<div class="btn" style="left:224px;top:401px;width:209px;height:42px">Make an Appointment</div>

<div class="feature" style="left:224px"><div class="dot" role="img" aria-label="Periodontology icon"></div><h4>PERIONTODOLOGY</h4><p>Lorem ipsum dolor sit amet<br>consectetur adipisicing elit.</p></div>
<div class="feature" style="left:480px"><div class="dot" role="img" aria-label="Tooth whitening icon"></div><h4>TOOTH WHITENING</h4><p>Lorem ipsum dolor sit amet<br>consectetur adipisicing elit.</p></div>
<div class="feature" style="left:736px"><div class="dot" role="img" aria-label="Preventative care icon"></div><h4>PREVENTATIVE CARE</h4><p>Lorem ipsum dolor sit amet<br>consectetur adipisicing elit.</p></div>

<!-- about -->
<div class="photo about-photo" role="img" aria-label="Smiling dentist in blue scrubs with a young girl in the dental chair"></div>
<div class="abs about-text">
  <div class="eyebrow">What we do?</div>
  <div class="heading">About Us</div>
  <p>Lorem ipsum dolor sit amet, consectetur adipiscing elit. Duis semper venenatis turpis eget suscipit. Orci varius natoque penatibus et magnis dis parturient montes, nascetur ridiculus mus. Donec eu nulla sollicitudin, vestibulum sapien nec, dictum dolor. Morbi non penatibus et magnis volutpat magna.Orci varius natoque penatibus et magnis dis parturient montes, nascetur ridiculus mus. Donec eu nulla sollicitudin.</p>
</div>
<div class="btn" style="left:494px;top:853px;width:115px;height:42px">View More</div>

<!-- services -->
<div class="abs services-head">
  <div class="eyebrow">Our services</div>
  <div class="heading">Our Dent<b>al Services</b></div>
</div>
<div class="abs services-band"></div>
<div class="abs service-grid">
  <div class="service active"><div class="icon" role="img" aria-label="Crown icon"></div><h3>Crowns Bridges</h3><p>Lorem ipsum dolor sit amet,<br>consectetur adipiscing elit.<br>Duis sem per venenatis turpis.</p><div class="bar"></div></div>
  <div class="service"><div class="icon" role="img" aria-label="Implant icon"></div><h3>Implants</h3><p>Lorem ipsum dolor sit amet,<br>consectetur adipiscing elit.<br>Duis sem per venenatis turpis.</p></div>
  <div class="service"><div class="icon" role="img" aria-label="Whitening icon"></div><h3>Teeth Whitening</h3><p>Lorem ipsum dolor sit amet,<br>consectetur adipiscing elit.<br>Duis sem per venenatis turpis.</p></div>
  <div class="service"><div class="icon" role="img" aria-label="Root canal icon"></div><h3>Root Canals</h3><p>Lorem ipsum dolor sit amet,<br>consectetur adipiscing elit.<br>Duis sem per venenatis turpis.</p></div>
  <div class="service"><div class="icon" role="img" aria-label="Wisdom teeth icon"></div><h3>Wisdom Teeths</h3><p>Lorem ipsum dolor sit amet,<br>consectetur adipiscing elit.<br>Duis sem per venenatis turpis.</p></div>
  <div class="service"><div class="icon" role="img" aria-label="Braces icon"></div><h3>Braces</h3><p>Lorem ipsum dolor sit amet,<br>consectetur adipiscing elit.<br>Duis sem per venenatis turpis.</p></div>
  <div class="service"><div class="icon" role="img" aria-label="Tooth icon"></div><h3>Implant Dentistry</h3><p>Lorem ipsum dolor sit amet,<br>consectetur adipiscing elit.<br>Duis sem per venenatis turpis.</p></div>
  <div class="service"><div class="icon" role="img" aria-label="Dental tools icon"></div><h3>Dentist Tools</h3><p>Lorem ipsum dolor sit amet,<br>consectetur adipiscing elit.<br>Duis sem per venenatis turpis.</p></div>
</div>

<!-- newsletter -->
<div class="abs newsletter">
  <h2>Newsletter</h2>
  <div class="field-mail">E-Mail</div>
  <div class="submit">Submit</div>
</div>

<!-- patients -->
<div class="abs patient-text">
  <div class="eyebrow">Our Patient</div>
  <div class="heading">Our Happ<b>y Patient</b></div>
  <p>Lorem ipsum dolor sit amet, consectetur adipiscing elit. Duis sem per venenatis turpis.Lorem ipsum dolor sit amet, consectetur adipiscing elit. Duis sem per venenatis turpis.</p>
</div>
<div class="btn" style="left:226px;top:2133px;width:116px;height:43px">View More</div>
<div class="abs pattern-area" role="img" aria-label="Light decorative pattern backdrop"></div>
<div class="abs patient-frame"></div>
<div class="photo patient-one" role="img" aria-label="Portrait of a smiling patient"></div>
<div class="patient-card"><h5>Marella T.</h5><p>Tooth Whitening, Root Canal<br>Treatments, Implants</p><span>View More</span></div>
<div class="photo patient-two" role="img" aria-label="Portrait of a smiling patient wearing glasses"></div>
<div class="abs patient-two-name">Ivana Corvel</div>

<!-- care -->
<div class="abs care-bg" role="img" aria-label="Faint dental icon pattern backdrop"></div>
<div class="photo care-photo" role="img" aria-label="Dentist in mask treating a female patient"></div>
<div class="abs care-text">
  <div class="heading">Complete Dent<b>al Care</b></div>
  <h4>Lorem ipsum dolor sit amet, consectetur adipiscing elit. Duis sem per venenatis turpis.</h4>
  <p>Lorem ipsum dolor sit amet, consectetur adipiscing elit. Duis sem per venenatis turpis.Lorem ipsum dolor sit amet, consectetur adipiscing elit. Duis sem per venenatis turpis.</p>
</div>
<div class="btn" style="left:601px;top:2636px;width:117px;height:43px">View More</div>

<!-- appointment -->
<div class="abs appoint-bg"></div>
<div class="photo family-photo" role="img" aria-label="Father, mother and daughter brushing their teeth"></div>
<div class="abs heading appoint-title">Make an <b>Appointment</b></div>
<div class="input" style="left:224px;top:2826px;width:174px;height:38px">Name</div>
<div class="input" style="left:424px;top:2826px;width:174px;height:38px">Phone no</div>
<div class="input" style="left:224px;top:2873px;width:374px;height:41px">Email</div>
<div class="input" style="left:224px;top:2922px;width:374px;height:81px">Message</div>
<div class="btn" style="left:224px;top:3018px;width:115px;height:41px">Send</div>

<!-- news -->
<div class="abs heading news-title">Latest <b>News</b></div>
<div class="news-card" style="left:224px"><div class="pic" role="img" aria-label="Receptionist smiling on the phone" style="background:linear-gradient(135deg,#e9eef2,#d7c3b4 55%,#f1f1f1)"></div><div class="date">June 13 - 6:00 pm-8:00</div><h5>Lorem ipsum dolor sit amet, consectetur</h5><a>Read More</a></div>
<div class="news-card" style="left:413px"><div class="pic" role="img" aria-label="Patient having a dental check-up" style="background:linear-gradient(135deg,#6e7a82,#c9a592 55%,#8d98a0)"></div><div class="date">June 13 - 6:00 pm-8:00</div><h5>Lorem ipsum dolor sit amet, consectetur</h5><a>Read More</a></div>
<div class="news-card" style="left:601px"><div class="pic" role="img" aria-label="Dentist examining a smiling patient" style="background:linear-gradient(135deg,#dfe9f1,#8cc3e3 50%,#e5c9b8)"></div><div class="date">June 13 - 6:00 pm-8:00</div><h5>Lorem ipsum dolor sit amet, consectetur</h5><a>Read More</a></div>
<div class="news-card" style="left:789px"><div class="pic" role="img" aria-label="Close-up of a smile with a dental brush" style="background:linear-gradient(135deg,#efd7cc,#d48b86 50%,#f4e4dc)"></div><div class="date">June 13 - 6:00 pm-8:00</div><h5>Lorem ipsum dolor sit amet, consectetur</h5><a>Read More</a></div>
<div class="btn" style="left:542px;top:3448px;width:115px;height:41px">View More</div>

<!-- footer -->
<div class="abs footer"></div>
<div class="abs footer-logo">Brivon</div>
<div class="abs footer-about">Lorem ipsum dolor sit amet, consectetur adipiscing elit. Duis sem per venenatis turpis.Lorem</div>
<div class="social" style="left:225px" role="img" aria-label="Social link"></div>
<div class="social" style="left:258px" role="img" aria-label="Social link"></div>
<div class="social" style="left:292px" role="img" aria-label="Social link"></div>

<div class="col-title" style="left:486px">Quick Link</div>
<div class="abs quick">Home<br>Services<br>About Us<br>News</div>

<div class="col-title" style="left:604px">Contact Us</div>
<div class="contact-row" style="top:3682px">
  <svg width="12" height="16" viewBox="0 0 12 16"><path d="M6 0C2.7 0 0 2.6 0 5.9 0 10.3 6 16 6 16s6-5.7 6-10.1C12 2.6 9.3 0 6 0zm0 8.2A2.3 2.3 0 1 1 6 3.6a2.3 2.3 0 0 1 0 4.6z" fill="#fff"/></svg>
  <span>Lorem ipsum street,<br>1800 dolor City</span>
</div>
<div class="contact-row" style="top:3724px">
  <svg width="16" height="12" viewBox="0 0 16 12"><rect x="0.5" y="0.5" width="15" height="11" fill="none" stroke="#fff"/><path d="M1 1l7 6 7-6" fill="none" stroke="#fff"/></svg>
  <span>demo@example.com</span>
</div>
<div class="contact-row" style="top:3754px">
  <svg width="13" height="13" viewBox="0 0 13 13"><path d="M2.6 0.5l2.2 2.6-1.2 1.6c.8 1.8 2.2 3.2 4 4l1.6-1.2 2.6 2.2-1 2.3C5.4 12 1 7.6 0.3 2.1z" fill="#fff"/></svg>
  <span>(480) 555-0142</span>
</div>

<div class="abs hours">
  <h6>Opening Hours</h6>
  <table>
    <tr><td>Monday</td><td>8:00am - 12:00pm</td></tr>
    <tr><td>Tuesday</td><td>8:00am - 12:00pm</td></tr>
    <tr><td>Wednesday</td><td>8:00am - 12:00pm</td></tr>
    <tr><td>Thursday</td><td>8:00am - 12:00pm</td></tr>
    <tr><td>Friday</td><td>8:00am - 12:00pm</td></tr>
    <tr><td>Sunday</td><td>8:00am - 12:00pm</td></tr>
  </table>
</div>
<div class="abs footer-rule"></div>
<div class="abs copyright">copyright © 2019 . All rights reserved.</div>

</body>
</html>
```